Trade show vertical and horizontal banners for large precision optics company

We will attend a trade show later this year. For the show we are using a Texas Flag theme. The carpet color for our booth will be red and the sidewalls will be dark blue. We need TWO banners for our booth and want them to not blend in with the booth itself. Our website is www.pelmorvisionworks.com

The first is a vertical design that can be printed on to a retractable banner 33 inches wide by 66 inches long.

Print specifications: http://www.quonsignprint.com/content/downloads/33x80RetractableQSP.pdf

We make large mirrors up to 36 inches in diameter. We want a picture of a mirror, or perhaps an abstract representation such as a curved shape or change in color in the central area of the banner where text can be placed. The banner needs to have our name (Pelmor Vision Works) at the top, a listing of our main products in the middle, and our logo towards the bottom. The goal of this banner is to get our company name and product offerings front and center in the booth in order to draw people in.

The second is a horizontal design that can be printed on a 96x96 inch banner.

Print specifications:
http://www.quonsignprint.com/content/downloads/96x96_LargeAdjustableBannerQSP.pdf

This banner will go along the back of the booth. It's purpose is to highlight our company name. The vertical banner (above) will be in the front of the booth on the left hand side. Therefore, we would like the company name to be towards the right hand side of the banner so that it can be seen. We would like both banners to be similar in theme.

This is the print specification file for the table throw. http://files.drelvamark.com/templates/Standard-Rectangular-Table-Throw-with-Full-Print_4ft_Economy-Coverage_R1.PDF&mode=view

Target Market(s)

flight simulators, large format projection systems

Industry/Entity Type

Flag

Colors
0355a3
ec1f27
ffffff

Requirements
Must have
• A clear statement of our company name, logo, and offerings. Eye catching graphics that will make people stop and look at our trade show booth.
Nice to have
• Texas flag theme (red white and blue) Additional colors can be used as long as they match with the overall theme.

```html
<!DOCTYPE html>
<html lang="en">
<head>
<meta charset="utf-8">
<title>Pelmor Vision Works – Precision Mirrors Banner</title>
<link rel="stylesheet" href="https://fonts.googleapis.com/css2?family=Arimo:wght@400;700&family=Tinos:ital,wght@0,700;1,700&display=swap">
<style>
  :root {
    --blue-deep: #0a3a94;
    --blue-mid: #1457bd;
    --blue-bright: #2f78dc;
    --blue-pale: #4f93ea;
    --red: #ec1f27;
    --red-tag: #e3202b;
    --white: #ffffff;
    --silver: #b9c3cf;
  }
  * { margin: 0; padding: 0; box-sizing: border-box; }
  html, body { width: 1200px; height: 2400px; overflow: hidden; background: var(--blue-deep); }
  .banner {
    position: relative;
    width: 1200px;
    height: 2400px;
    overflow: hidden;
    background: linear-gradient(180deg, var(--blue-mid) 0%, var(--blue-deep) 45%, #0b3c9c 100%);
    font-family: "Arimo", Arial, sans-serif;
    color: var(--white);
  }
  .backdrop { position: absolute; inset: 0; width: 1200px; height: 2400px; }
  .headline {
    position: absolute;
    font-family: "Arimo", Arial, sans-serif;
    font-weight: 700;
    color: var(--white);
    text-shadow: 4px 4px 0 var(--red), -1px -1px 0 rgba(236,31,39,.6);
    line-height: 1;
    white-space: nowrap;
  }
  .headline--line1 { left: 150px; top: 210px; font-size: 98px; }
  .headline--large { left: 760px; top: 300px; font-size: 90px; }
  .headline--precision { left: 140px; top: 410px; font-size: 108px; }
  .headline--mirrors { left: 650px; top: 440px; font-size: 108px; }

  .products { position: absolute; left: 160px; top: 1000px; font-family: "Tinos", "Times New Roman", serif; font-weight: 700; }
  .products__title { font-size: 74px; letter-spacing: 1px; margin-bottom: 52px; }
  .products__list { list-style: none; }
  .products__item { font-size: 58px; line-height: 104px; padding-left: 48px; position: relative; white-space: nowrap; }
  .products__item::before { content: "•"; position: absolute; left: 0; }

  .brand { position: absolute; left: 0; top: 1700px; width: 1200px; text-align: center; }
  .brand__mark {
    display: block; margin: 0 auto;
    width: 260px; height: 260px; border-radius: 50%;
    background: var(--silver);
  }
  .brand__name { margin-top: 44px; font-size: 54px; font-weight: 700; }

  .tagline {
    position: absolute; left: 0; top: 2130px; width: 1200px; text-align: center;
    font-family: "Tinos", "Times New Roman", serif; font-style: italic; font-weight: 700;
    font-size: 72px; line-height: 92px; color: var(--red-tag);
  }
</style>
</head>
<body>
<main class="banner">
  <svg class="backdrop" viewBox="0 0 1200 2400" aria-hidden="true">
    <defs>
      <linearGradient id="swoosh" x1="0" y1="0" x2="0" y2="1">
        <stop offset="0" stop-color="#3a84e6"/>
        <stop offset="1" stop-color="#1a5fca"/>
      </linearGradient>
      <radialGradient id="mirror" cx="0.55" cy="0.45" r="0.6">
        <stop offset="0" stop-color="#3f7fd8" stop-opacity=".55"/>
        <stop offset="1" stop-color="#1b5ac2" stop-opacity=".35"/>
      </radialGradient>
    </defs>
    <path class="backdrop__top" d="M0 0 H1200 V140 C900 260 500 560 0 720 Z" fill="#1656c0"/>
    <path class="backdrop__swoosh" d="M1200 40 C1000 380 600 700 0 760 L0 900 C500 830 900 900 1200 1020 Z" fill="url(#swoosh)"/>
    <path class="backdrop__swoosh-edge" d="M0 900 C500 830 900 900 1200 1020 L1200 1040 C900 930 500 860 0 930 Z" fill="#4f93ea" opacity=".7"/>
    <circle class="backdrop__mirror" cx="110" cy="1290" r="340" fill="url(#mirror)" stroke="#cfe0f7" stroke-opacity=".7" stroke-width="6"/>
  </svg>

  <h1 class="headline-group">
    <span class="headline headline--line1">We manufacture</span>
    <span class="headline headline--large">large</span>
    <span class="headline headline--precision">Precision</span>
    <span class="headline headline--mirrors">Mirrors!</span>
  </h1>

  <section class="products">
    <h2 class="products__title">OUR PRODUCTS</h2>
    <ul class="products__list">
      <li class="products__item">Collimating mirrors</li>
      <li class="products__item">Wide angle collimating mirrors</li>
      <li class="products__item">High quality spherical mirrors</li>
      <li class="products__item">Flat fold mirrors</li>
      <li class="products__item">Beam splitters</li>
    </ul>
  </section>

  <div class="brand">
    <span class="brand__mark" aria-hidden="true"></span>
    <p class="brand__name">Pelmor Vision Works</p>
  </div>

  <p class="tagline">making a difference<br>in the World of Optics !</p>
</main>
</body>
</html>
```